Professional Services (B-2-B) Business Cards (Front & Back)

Quintarion is a business-to-business professional services company in the legal sector. They typically present to c-suite and executive functions who are looking for providers with expertise, and experience. Our business card should look and feel professional and contemporary, but we are not a startup tech company, so we want the tone to be more mature.

```html
<!DOCTYPE html>
<html lang="en">
<head>
<meta charset="utf-8">
<title>Quintarion Business Cards</title>
<link href="https://fonts.googleapis.com/css2?family=Montserrat:wght@400;500;700&display=swap" rel="stylesheet">
<style>
  :root {
    --backdrop: #e7e5e2;
    --card-navy: #1e3266;
    --card-navy-deep: #1a2c5b;
    --ink-white: #ffffff;
    --rule-soft: rgba(255,255,255,0.6);
  }
  * { box-sizing: border-box; margin: 0; padding: 0; }
  html, body {
    width: 1200px; height: 984px; overflow: hidden;
    background: var(--backdrop);
    font-family: "Montserrat", Arial, sans-serif;
    color: var(--ink-white);
  }
  .canvas { position: relative; width: 1200px; height: 984px; }
  .card {
    position: absolute; left: 160px; width: 880px; height: 420px;
    background: linear-gradient(135deg, var(--card-navy) 0%, var(--card-navy-deep) 100%);
    box-shadow: 0 6px 18px rgba(0,0,0,0.18);
    overflow: hidden;
  }
  .card--front { top: 52px; }
  .card--back { top: 512px; }

  .wordmark {
    font-weight: 500; text-transform: uppercase; letter-spacing: 0.42em; white-space: nowrap;
  }
  .card--front .wordmark { position: absolute; left: 46px; top: 48px; font-size: 18px; }
  .person { position: absolute; left: 46px; top: 112px; }
  .person__name { font-size: 30px; font-weight: 700; letter-spacing: 0.01em; }
  .person__role { font-size: 16px; font-weight: 400; margin-top: 2px; }
  .person__bar { width: 26px; height: 3px; background: var(--ink-white); margin-top: 14px; }
  .contact { position: absolute; left: 46px; top: 222px; list-style: none; font-size: 17px; line-height: 30px; }
  .divider-long {
    position: absolute; left: 46px; right: 46px; top: 214px; height: 1px;
    background: var(--rule-soft);
  }
  .divider-long::after {
    content: ""; position: absolute; left: 62%; top: -1px; width: 26px; height: 3px;
    background: var(--ink-white);
  }
  .address { position: absolute; right: 60px; bottom: 46px; font-size: 17px; line-height: 26px; font-style: normal; }

  .card--back .wordmark {
    position: absolute; left: 0; right: 0; top: 120px; text-align: center; font-size: 36px;
  }
  .divider-center {
    position: absolute; left: 110px; right: 110px; top: 206px; height: 1px; background: var(--rule-soft);
  }
  .tagline {
    position: absolute; left: 0; right: 0; top: 232px; text-align: center;
    font-size: 19px; line-height: 32px; font-weight: 400; letter-spacing: 0.02em;
  }
</style>
</head>
<body>
<main class="canvas">
  <section class="card card--front" aria-label="Business card front">
    <div class="wordmark">Quintarion</div>
    <div class="person">
      <div class="person__name">Marcus Hale</div>
      <div class="person__role">President &amp; CEO</div>
      <div class="person__bar"></div>
    </div>
    <div class="divider-long"></div>
    <ul class="contact">
      <li>Phone: (415) 555 – 0142</li>
      <li>Office: (203) 555 – 0187</li>
      <li>www.quintarion.tech</li>
      <li>mhale@quintarion.tech</li>
    </ul>
    <address class="address">
      QUINTARION<br>
      #410, 88 Harbor Street<br>
      Somewhere in the country
    </address>
  </section>

  <section class="card card--back" aria-label="Business card back">
    <div class="wordmark">Quintarion</div>
    <div class="divider-center"></div>
    <p class="tagline">Guiding legal leaders toward measurable, lasting cost control<br>Strategic Legal Advisory Partners</p>
  </section>
</main>
</body>
</html>
```